Design for a 4 screens mobile app: Brightnook

The app is a compact but illustrated phone/address book...
We need a design for the 5 screens of the app (see screens attached):
a) "index" : 1 screen with 6 pictures of contact person
b) "contact list" : 1 screen, to manage (add/del/edit) the contacts of the phone/address book
c) "add contact" : 1 screen to add a contact (a picture + a phone number)
d) "update contact" : similar to "add"
e) "fields missing" : add/edit screens in "error" state
We also need the ico design + loading screen.
No specific guidelines, nor logo or whatever.
It will be a free app distributed on iOS and Androïd.
We just want to make it looking nice & very usable for end users.
B2C

```html
<!DOCTYPE html>
<html lang="en">
<head>
<meta charset="utf-8">
<title>Brightnook – Update Contact Screen</title>
<link href="https://fonts.googleapis.com/css2?family=Exo+2:wght@200;300;400;500;600&display=swap" rel="stylesheet">
<style>
  :root {
    --sky: #04bbf0;
    --sky-text: #19b5e8;
    --deep-blue: #0f6d97;
    --ring-blue: #1a6f96;
    --paper: #ffffff;
    --ink: #1d1d1d;
    --label: #8a8a8a;
    --field-border: #b9b9b9;
    --meadow: #1f8a4c;
    --confirm: #1c5e3a;
    --confirm-tick: #2fe06a;
    --cancel: #9c2127;
    --cancel-x: #e23a3a;
  }
  * { margin: 0; padding: 0; box-sizing: border-box; }
  html, body { width: 1200px; height: 699px; overflow: hidden; background: var(--paper); }
  body { position: relative; font-family: "Exo 2", sans-serif; }

  .backdrop-band { position: absolute; inset: 0; }

  .showcase-title { position: absolute; left: 138px; top: 308px; color: var(--sky-text); }
  .showcase-title .app-name { font-size: 26px; font-weight: 500; letter-spacing: 0.3px; }
  .showcase-title .screen-name { font-size: 55px; font-weight: 200; line-height: 66px; margin-top: 12px; letter-spacing: 1px; }

  .app-screen { position: absolute; left: 823px; top: 107px; width: 275px; height: 491px; background: var(--paper); overflow: hidden; }
  .screen-shapes { position: absolute; inset: 0; }

  .status-bar { position: absolute; left: 0; top: 0; width: 100%; height: 20px; display: flex; align-items: center; justify-content: space-between; padding: 0 6px; color: var(--paper); font-size: 9.5px; font-family: "Exo 2", sans-serif; font-weight: 500; }
  .status-time { position: absolute; left: 50%; transform: translateX(-50%); font-weight: 600; }

  .screen-title { position: absolute; left: 12px; top: 46px; color: var(--paper); font-size: 17px; font-weight: 600; }

  .field-label { position: absolute; left: 0; width: 100%; text-align: center; font-size: 10px; color: var(--label); }
  .text-field { position: absolute; left: 16px; width: 245px; height: 39px; border: 1px solid var(--field-border); border-radius: 10px; display: flex; align-items: center; justify-content: space-between; padding: 0 12px 0 10px; font-size: 18px; color: var(--ink); font-weight: 400; }

  .avatar { position: absolute; left: 79px; top: 114px; width: 116px; height: 116px; border-radius: 50%; border: 3px solid var(--ring-blue); background: radial-gradient(circle at 45% 40%, #f1c79a 0%, #d99a62 45%, #c9b8a4 75%, #e9e2d8 100%); }
</style>
</head>
<body>
  <svg class="backdrop-band" width="1200" height="699" aria-hidden="true">
    <polygon points="240,0 1200,0 1200,172" fill="var(--sky)"/>
  </svg>

  <div class="showcase-title">
    <p class="app-name">Brightnook App Design</p>
    <h1 class="screen-name">UPDATE CONTACT<br>SCREEN</h1>
  </div>

  <main class="app-screen">
    <svg class="screen-shapes" width="275" height="491" aria-hidden="true">
      <polygon points="0,0 275,0 275,58 0,103" fill="var(--sky)"/>
      <polygon points="0,478 275,430 275,491 0,491" fill="var(--meadow)"/>
      <!-- back button -->
      <circle cx="225" cy="65" r="24" fill="var(--deep-blue)" stroke="var(--paper)" stroke-width="2.5"/>
      <path d="M235 65 H216 M223 57 L215 65 L223 73" stroke="#9fdcf3" stroke-width="3" fill="none" stroke-linecap="round" stroke-linejoin="round"/>
      <!-- cancel -->
      <circle cx="162" cy="449" r="23" fill="var(--cancel)" stroke="var(--paper)" stroke-width="2.5"/>
      <path d="M155 442 L169 456 M169 442 L155 456" stroke="var(--cancel-x)" stroke-width="3.5" stroke-linecap="round"/>
      <!-- confirm -->
      <circle cx="225" cy="439" r="23" fill="var(--confirm)" stroke="var(--paper)" stroke-width="2.5"/>
      <path d="M216 440 L222 446 L234 433" stroke="var(--confirm-tick)" stroke-width="4" fill="none" stroke-linecap="round" stroke-linejoin="round"/>
    </svg>

    <div class="status-bar">
      <span>●●●○○ NOVA</span>
      <span class="status-time">4:21 PM</span>
      <span>22% ▭</span>
    </div>

    <h2 class="screen-title">Update Contact</h2>

    <p class="field-label" style="top:96px">Upload Picture</p>
    <div class="avatar" role="img" aria-label="Contact portrait photo"></div>
    <svg style="position:absolute;left:0;top:0" width="275" height="260" aria-hidden="true">
      <circle cx="157" cy="231" r="17" fill="var(--deep-blue)" stroke="var(--paper)" stroke-width="2"/>
      <rect x="150" y="224" width="14" height="14" rx="1.5" fill="none" stroke="var(--paper)" stroke-width="1.6"/>
      <path d="M151 236 L155 231 L158 234 L160 232 L163 236 Z" fill="var(--paper)"/>
      <circle cx="185" cy="214" r="17" fill="var(--deep-blue)" stroke="var(--paper)" stroke-width="2"/>
      <rect x="177" y="209" width="16" height="11" rx="2" fill="var(--paper)"/>
      <rect x="181" y="206.5" width="7" height="3" rx="1" fill="var(--paper)"/>
      <circle cx="185" cy="214.5" r="3.3" fill="var(--deep-blue)"/>
    </svg>

    <p class="field-label" style="top:253px">Name</p>
    <div class="text-field" style="top:272px">
      <span>Marisol Vance</span>
      <svg width="14" height="14" aria-hidden="true"><path d="M2 12 L3 9 L10 2 L12 4 L5 11 Z" fill="none" stroke="#8c8c8c" stroke-width="1.3"/></svg>
    </div>

    <p class="field-label" style="top:324px">Phone Number</p>
    <div class="text-field" style="top:343px">
      <span>555018273645</span>
      <svg width="14" height="14" aria-hidden="true"><path d="M2 12 L3 9 L10 2 L12 4 L5 11 Z" fill="none" stroke="#8c8c8c" stroke-width="1.3"/></svg>
    </div>
  </main>
</body>
</html>
```